Brochure Annual Report Design

I want to create a brochure / annual report for our company. Can you help me. I like this design. https://plumvaultdesigns.net/Zorvik/4829175-Annual-Report-2018. Here is our company website www.brimdental.com. Please take the logo from there. Our website needs an upgrade in how it looks. I would like the brochure annual report and the website to look somewhat congruent. I also want to create a very high end magazine that is fun for our company eventually.

We are a company that helps dentists create better practices by really improving the way they do business and motivating their teams. As a result they have more fun, more profit, happier team members, and they all have better lives.

Target Market(s)

dentist

Industry/Entity Type

Dental

Number of Pages Required

5+ page

Colors
0255a3
85cae6
ffffff

Requirements
Must have
• Must look really good.
Nice to have
• Any creative suggestions are welcomed. I need a website that looks congruent to the brochure and annual report. I also want to create a very high end magazine that is fun for our company eventually.
Should not have
• I don't like low quality design.

```html
<!DOCTYPE html>
<html lang="en">
<head>
<meta charset="utf-8">
<title>Brimdental Financial Report</title>
<link rel="stylesheet" href="https://fonts.googleapis.com/css2?family=Fira+Sans:wght@300;400;600;700;800&display=swap">
<style>
  :root {
    --brand-deep: #1b7cc1;
    --brand-sky: #85cae6;
    --brand-grey: #999a9c;
    --title-grey: #8a8b8d;
    --text: #3a3a3a;
    --accent-text: #2a90d0;
    --page: #f7f7f7;
    --white: #ffffff;
    --rule: #e2e2e2;
    --rule-dark: #333333;
  }
  * { box-sizing: border-box; margin: 0; padding: 0; }
  html, body { width: 848px; height: 1200px; overflow: hidden; background: var(--white); }
  body { position: relative; font-family: "Fira Sans", sans-serif; color: var(--text); }

  .brand { position: absolute; left: 76px; top: 40px; font-size: 32px; font-weight: 600; color: var(--brand-deep); letter-spacing: -0.5px; }

  .page-body { position: absolute; left: 0; top: 97px; width: 848px; height: 1007px; background: var(--page); }

  .title-bar { position: absolute; left: 72px; top: 138px; width: 11px; height: 82px; background: var(--brand-sky); }
  .title-main { position: absolute; left: 88px; top: 120px; font-size: 66px; font-weight: 700; color: var(--brand-sky); line-height: 1; letter-spacing: -0.5px; }
  .title-sub { position: absolute; left: 89px; top: 184px; font-size: 41px; font-weight: 700; color: var(--title-grey); line-height: 1; }

  .stat { position: absolute; top: 268px; width: 212px; height: 162px; color: var(--white); text-align: center; }
  .stat--markets { left: 89px; background: var(--brand-sky); }
  .stat--sales { left: 318px; background: var(--brand-grey); }
  .stat--global { left: 547px; background: var(--brand-deep); }
  .stat-label { margin-top: 32px; font-size: 22px; font-weight: 700; line-height: 1; }
  .stat-period { font-size: 11px; font-weight: 600; margin-top: 1px; }
  .stat-value { font-size: 35px; font-weight: 700; margin-top: 8px; line-height: 1.1; }
  .stat-note { font-size: 11px; font-weight: 400; margin-top: 3px; }
  .stat--markets .stat-note { font-weight: 600; }

  .data-table { position: absolute; width: 327px; font-size: 12px; }
  .col-left { left: 89px; }
  .col-right { left: 432px; }
  .row { display: grid; grid-template-columns: 209px 63px 1fr; align-items: center; height: 33px; padding-left: 12px; border-bottom: 1px solid var(--rule); }
  .row span:first-child { padding-right: 6px; }
  .row--head { height: 32px; border-bottom: 1.5px solid var(--rule-dark); color: var(--accent-text); padding-left: 18px; grid-template-columns: 203px 65px 1fr; }
  .row--total { color: var(--accent-text); border-bottom: 1.5px solid var(--accent-text); grid-template-columns: 203px 60px 1fr; }
  sup { font-size: 8px; }

  .folio { position: absolute; left: 79px; top: 1133px; font-size: 16px; font-weight: 700; color: #222; }
  .folio-rule { position: absolute; left: 125px; top: 1143px; width: 656px; height: 1px; background: #8fa0b3; }
</style>
</head>
<body>
  <div class="brand">Brimdental</div>

  <main class="page-body"></main>

  <div class="title-bar"></div>
  <h1 class="title-main">FINANCIAL</h1>
  <h2 class="title-sub">REPORT</h2>

  <section class="stat stat--markets">
    <div class="stat-label">THE MARKETS</div>
    <div class="stat-period">Since March 2017</div>
    <div class="stat-value">$321.789</div>
    <div class="stat-note">greater profit than 2014</div>
  </section>
  <section class="stat stat--sales">
    <div class="stat-label">NET SALES</div>
    <div class="stat-period">Last quater of 2016</div>
    <div class="stat-value">+$44.178</div>
    <div class="stat-note">in the sector hardware</div>
  </section>
  <section class="stat stat--global">
    <div class="stat-label">GLOBAL MARKET</div>
    <div class="stat-period">Volume export 2016</div>
    <div class="stat-value">$102.098</div>
    <div class="stat-note">in all areas</div>
  </section>

  <div class="data-table col-left" style="top:466px">
    <div class="row row--head"><span>Year ended December 31<sup>st</sup></span><span>Sales</span><span>Percent</span></div>
    <div class="row"><span>Quae verfernam rem</span><span>1.290</span><span>25%</span></div>
    <div class="row"><span>Sedis as plaborem nus, ipsa sunt</span><span>3.456</span><span>47%</span></div>
    <div class="row"><span>Ibusandae porest audae</span><span>2.785</span><span>38%</span></div>
    <div class="row"><span>Parum nis mosti re et pariandit</span><span>980</span><span>8%</span></div>
    <div class="row"><span>Eperehe ndamuscia est</span><span>6.312</span><span>56%</span></div>
    <div class="row"><span>Beaquatia prest, alite eaquassi</span><span>456</span><span>5%</span></div>
    <div class="row row--total"><span>Total</span><span>10.346</span><span>45%</span></div>
  </div>

  <div class="data-table col-left" style="top:775px">
    <div class="row row--head"><span>First quarter of 2017</span><span>Sales</span><span>Percent</span></div>
    <div class="row"><span>Quae verfernam rem</span><span>1.290</span><span>25%</span></div>
    <div class="row"><span>Sedis as plaborem nus, ipsa sunt</span><span>3.456</span><span>47%</span></div>
    <div class="row"><span>Ibusandae porest audae</span><span>2.785</span><span>38%</span></div>
    <div class="row"><span>Parum nis mosti re et pariandit</span><span>980</span><span>8%</span></div>
    <div class="row"><span>Eperehe ndamuscia est</span><span>6.312</span><span>56%</span></div>
    <div class="row"><span>Beaquatia prest, alite eaquassi</span><span>456</span><span>5%</span></div>
    <div class="row row--total"><span>Total</span><span>10.346</span><span>45%</span></div>
  </div>

  <div class="data-table col-right" style="top:466px">
    <div class="row row--head"><span>Financial Performace</span><span>Sales</span><span>Percent</span></div>
    <div class="row"><span>Quae verfernam rem</span><span>1.290</span><span>25%</span></div>
    <div class="row"><span>Sedis as plaborem nus, ipsa sunt</span><span>3.456</span><span>47%</span></div>
    <div class="row"><span>Beaquatia prest, alite eaquassi</span><span>456</span><span>5%</span></div>
    <div class="row row--total"><span>Total</span><span>10.346</span><span>45%</span></div>
  </div>

  <div class="data-table col-right" style="top:663px">
    <div class="row row--head"><span>Global Market</span><span>Sales</span><span>Percent</span></div>
    <div class="row"><span>Quae verfernam rem</span><span>1.290</span><span>25%</span></div>
    <div class="row"><span>Sedis as plaborem nus, ipsa sunt</span><span>3.456</span><span>47%</span></div>
    <div class="row"><span>Ibusandae porest audae</span><span>2.785</span><span>38%</span></div>
    <div class="row"><span>Parum nis mosti re et pariandit</span><span>980</span><span>8%</span></div>
    <div class="row row--total"><span>Total</span><span>10.346</span><span>45%</span></div>
  </div>

  <div class="data-table col-right" style="top:904px">
    <div class="row row--head"><span>Export to Europe</span><span>Sales</span><span>Percent</span></div>
    <div class="row"><span>Si duscipis et ut aut</span><span>1.290</span><span>25%</span></div>
    <div class="row"><span>Sequuntios et vollorehen</span><span>3.456</span><span>47%</span></div>
    <div class="row row--total"><span>Total</span><span>4.346</span><span>25%</span></div>
  </div>

  <div class="folio">24</div>
  <div class="folio-rule"></div>
</body>
</html>
```